Business Card Design

Our company is named Lumoplex which is an event ticketing company and our values are;

Fun/ Innovation/ Vibrancy / Integrity/ Community

In addition, we have a consumer facing platform which we use the brand - Zentabo

Project:
Design a business card template which is double sided
Side A - Lumoplex
Side B - Zentabo

Both logos of the company are attached.
Please keep within color tones however be creative with the design template.
We are open to having special die cut shape also.

Please don't hesitate to contact us for further information.

Thanks

```html
<!DOCTYPE html>
<html lang="en">
<head>
<meta charset="utf-8">
<title>Lumoplex / Zentabo Business Card</title>
<link rel="stylesheet" href="https://fonts.googleapis.com/css2?family=Oswald:wght@600&family=Montserrat:wght@800&family=Open+Sans:wght@400;600&display=swap">
<style>
  :root {
    --backdrop: #2b2b2d;
    --card: #1d1d1e;
    --paper: #ffffff;
    --ink: #111111;
    --accent: #c4161c;
    --muted: #e6e6e6;
    --rule: #4a4a4a;
  }
  * { box-sizing: border-box; margin: 0; padding: 0; }
  html, body { width: 1200px; height: 900px; overflow: hidden; }
  body {
    background: var(--backdrop);
    font-family: "Open Sans", Arial, sans-serif;
    position: relative;
  }
  .card {
    position: absolute;
    left: 340px;
    width: 520px;
    height: 300px;
    background: var(--card);
    overflow: hidden;
    box-shadow: 0 10px 30px rgba(0,0,0,.45);
  }
  .card--front { top: 120px; }
  .card--back { top: 470px; }

  .front__corner { position: absolute; inset: 0; }
  .front__brand {
    position: absolute;
    left: 56px;
    top: 118px;
    font-family: "Oswald", "Arial Narrow", sans-serif;
    font-weight: 600;
    font-size: 64px;
    letter-spacing: 1px;
    color: var(--paper);
    line-height: 1;
  }
  .front__address {
    position: absolute;
    right: 14px;
    top: 40px;
    text-align: right;
    font-family: Arial, "Open Sans", sans-serif;
    font-style: normal;
    font-size: 10.5px;
    line-height: 1.35;
    color: var(--ink);
  }

  .back__brand {
    position: absolute;
    left: 36px;
    top: 124px;
    display: flex;
    align-items: center;
    gap: 10px;
  }
  .back__brand-name {
    font-family: "Montserrat", Arial, sans-serif;
    font-weight: 800;
    font-size: 40px;
    color: var(--paper);
    line-height: 1;
  }
  .back__brand-mark {
    width: 22px;
    height: 22px;
    background: var(--accent);
  }
  .back__divider {
    position: absolute;
    left: 286px;
    top: 70px;
    width: 1px;
    height: 170px;
    background: var(--rule);
  }
  .back__details {
    position: absolute;
    left: 306px;
    top: 78px;
  }
  .back__name {
    font-weight: 600;
    font-size: 18px;
    color: var(--accent);
    margin-left: 40px;
    line-height: 1.1;
  }
  .back__role {
    font-size: 11px;
    color: var(--muted);
    margin-left: 40px;
    margin-bottom: 18px;
  }
  .contact-list { list-style: none; }
  .contact-list li {
    display: flex;
    align-items: center;
    gap: 10px;
    font-size: 12.5px;
    color: var(--muted);
    height: 22px;
  }
  .contact-list svg { width: 13px; height: 13px; flex: none; }
</style>
</head>
<body>

<section class="card card--front" aria-label="Lumoplex card side">
  <svg class="front__corner" viewBox="0 0 520 300" width="520" height="300" aria-hidden="true">
    <polygon points="300,0 520,0 520,200" fill="var(--paper)"/>
  </svg>
  <div class="front__brand">LUMOPLEX</div>
  <address class="front__address">
    0-00 Birchmont Crescent<br>Ottawa, ON K0A 0A0
  </address>
</section>

<section class="card card--back" aria-label="Zentabo card side">
  <div class="back__brand">
    <span class="back__brand-name">ZENTABO</span>
    <span class="back__brand-mark"></span>
  </div>
  <div class="back__divider"></div>
  <div class="back__details">
    <p class="back__name">Imran Talukder</p>
    <p class="back__role">SEO</p>
    <ul class="contact-list">
      <li>
        <svg viewBox="0 0 24 24" aria-hidden="true"><path fill="var(--accent)" d="M6.6 10.8a15 15 0 0 0 6.6 6.6l2.2-2.2a1 1 0 0 1 1-.25 11.4 11.4 0 0 0 3.6.57 1 1 0 0 1 1 1V20a1 1 0 0 1-1 1A17 17 0 0 1 3 4a1 1 0 0 1 1-1h3.5a1 1 0 0 1 1 1c0 1.25.2 2.45.57 3.57a1 1 0 0 1-.25 1z"/></svg>
        000000000
      </li>
      <li>
        <svg viewBox="0 0 24 24" aria-hidden="true"><circle cx="12" cy="12" r="9" fill="none" stroke="var(--accent)" stroke-width="2.5"/><circle cx="12" cy="12" r="3.5" fill="none" stroke="var(--accent)" stroke-width="2.5"/></svg>
        hello@zentabo.com
      </li>
      <li>
        <svg viewBox="0 0 24 24" aria-hidden="true"><circle cx="12" cy="12" r="9" fill="none" stroke="var(--accent)" stroke-width="2.5"/><path d="M3 12h18M12 3c3 3 3 15 0 18M12 3c-3 3-3 15 0 18" fill="none" stroke="var(--accent)" stroke-width="2"/></svg>
        www.zentabo.com
      </li>
    </ul>
  </div>
</section>

</body>
</html>
```